V STUDIO Interior & Exterior Designer Business needs a Business Card

V STUDIO - I need a Business Card Design for a Interior Design Business, I work Nationally Around Australia on Projects specialising In AGED CARE and would like to rebrand and change the Look.
I work mainly with Large Corporate Companys, Select everything From External Finishes to All Internal Finishes, Furniture and then Decorate to a 5 star finish.

Industry/Entity Type

Business

Contact Information for Business Card

V STUDIO
Marlene Oberly
PH: (+61) 0400 982 637
E: marly@vstudioinclub.com

Font styles to use
Sans Serif

Requirements
Must have
• My Priject Must Have a Contemporary Design, Bold, Eye Catching, that makes a statement but MUST BE ELEGANT - 2 or 3 Colours - Strong Power Colours.
• 2 sided
• i like the works - IMAGEN, DESIGN, CREATE
Nice to have
• I would like the words ' imagine design create ' incorporated into the design
• I like Some Red on the card

```html
<!DOCTYPE html>
<html lang="en">
<head>
<meta charset="utf-8">
<title>V STUDIO – Business Card</title>
<link href="https://fonts.googleapis.com/css2?family=Lato:wght@400;700;900&display=swap" rel="stylesheet">
<style>
  :root {
    --stage: #e4e5e8;
    --navy: #34445f;
    --navy-light: #4a5d80;
    --charcoal: #2c2d30;
    --charcoal-light: #3b3c40;
    --white: #ffffff;
    --ink: #1d1e22;
    --blue: #3b97d3;
    --red: #e52a2f;
    --gold: #cf9f2a;
    --brand-blue: #1f5fa8;
  }
  * { margin: 0; padding: 0; box-sizing: border-box; }
  html, body { width: 1200px; height: 890px; overflow: hidden; }
  body {
    background: var(--stage);
    font-family: "Lato", sans-serif;
    position: relative;
  }
  .card {
    position: absolute;
    left: 250px;
    width: 700px;
    height: 400px;
    overflow: hidden;
    background: linear-gradient(180deg, var(--charcoal-light), var(--charcoal));
    box-shadow: 0 6px 18px rgba(0,0,0,.18);
  }
  .card--back { top: 30px; }
  .card--front { top: 460px; }

  /* Back side */
  .back-sky {
    position: absolute; inset: 0 0 auto 0; height: 215px;
    background: linear-gradient(180deg, var(--navy-light), var(--navy));
  }
  .back-band { position: absolute; left: 0; top: 120px; width: 700px; height: 170px; }
  .brand {
    position: absolute; display: flex; align-items: center; gap: 10px;
    font-weight: 900; color: var(--brand-blue); letter-spacing: 1px;
  }
  .brand__dot { border-radius: 50%; background: var(--brand-blue); }
  .back-brand { left: 228px; top: 150px; font-size: 44px; }
  .back-brand .brand__dot { width: 46px; height: 46px; }
  .back-web {
    position: absolute; left: 0; width: 700px; top: 222px; text-align: center;
    font-weight: 900; font-size: 30px; color: var(--ink); letter-spacing: .5px;
  }

  /* Front side */
  .front-top { position: absolute; left: 0; top: 0; width: 700px; height: 140px; }
  .front-brand { right: 26px; top: 12px; font-size: 30px; }
  .front-brand .brand__dot { width: 34px; height: 34px; }
  .name-band {
    position: absolute; left: 0; top: 82px; width: 262px; height: 58px;
    background: var(--navy); color: var(--white);
    font-weight: 700; font-size: 25px; line-height: 58px; padding-left: 18px;
  }
  .name-marks { position: absolute; left: 18px; top: 140px; display: flex; gap: 4px; }
  .name-marks span { width: 14px; height: 4px; }
  .tile {
    position: absolute; color: var(--white); font-size: 15px;
    display: flex; flex-direction: column; align-items: center; justify-content: center; gap: 12px;
  }
  .tile svg { width: 26px; height: 26px; }
  .tile--email { left: 266px; top: 62px; width: 214px; height: 140px; background: var(--blue); }
  .tile--web { left: 484px; top: 62px; width: 216px; height: 140px; background: var(--red); }
  .tile--phone { left: 0; top: 150px; width: 262px; height: 125px; background: var(--gold); font-size: 17px; }
  .rule { position: absolute; height: 2px; background: var(--blue); opacity: .8; }
  .rule--upper { left: 270px; top: 236px; width: 410px; }
  .rule--lower { left: 20px; top: 384px; width: 560px; }
  .address {
    position: absolute; left: 22px; top: 296px; color: var(--white);
    font-size: 19px; line-height: 30px;
  }
</style>
</head>
<body>

<section class="card card--back" aria-label="Business card, back side">
  <div class="back-sky"></div>
  <svg class="back-band" viewBox="0 0 700 170" aria-hidden="true">
    <path d="M150 20 H550 L575 45 Q585 58 600 58 H640 V130 H600 Q585 130 575 143 L560 160 H140 L125 143 Q115 130 100 130 H60 V58 H100 Q115 58 125 45 Z" fill="var(--white)"/>
  </svg>
  <div class="brand back-brand"><span class="brand__dot"></span>V STUDIO</div>
  <div class="back-web">WWW.VSTUDIOINCLUB.COM</div>
</section>

<section class="card card--front" aria-label="Business card, front side">
  <svg class="front-top" viewBox="0 0 700 140" aria-hidden="true">
    <path d="M0 0 H700 V62 H380 L340 82 H0 Z" fill="var(--white)"/>
  </svg>
  <div class="brand front-brand"><span class="brand__dot"></span>V STUDIO</div>

  <div class="name-band">Marlene Oberly</div>
  <div class="name-marks">
    <span style="background:var(--red)"></span>
    <span style="background:var(--blue)"></span>
    <span style="background:var(--gold)"></span>
  </div>

  <div class="tile tile--email">
    <svg viewBox="0 0 24 24" aria-hidden="true"><rect x="2" y="5" width="20" height="14" fill="var(--white)"/><path d="M2 5 L12 13 L22 5" fill="none" stroke="var(--blue)" stroke-width="1.6"/></svg>
    <span>marly@vstudioinclub.com</span>
  </div>
  <div class="tile tile--web">
    <svg viewBox="0 0 24 24" aria-hidden="true" fill="none" stroke="var(--white)" stroke-width="1.6"><circle cx="12" cy="12" r="9"/><ellipse cx="12" cy="12" rx="4" ry="9"/><path d="M3 12 H21 M5 7 H19 M5 17 H19"/></svg>
    <span>vstudioinclub.com</span>
  </div>
  <div class="tile tile--phone">
    <svg viewBox="0 0 24 24" aria-hidden="true"><path d="M6.6 3 L9.5 6.5 L7.8 9 Q9.5 12.8 14.8 16.2 L17.3 14.5 L21 17.4 L19 20.5 Q12 21 6.6 14.6 Q2.5 9 3.6 5 Z" fill="var(--white)"/></svg>
    <span>(+61) 0400 982 637</span>
  </div>

  <div class="rule rule--upper"></div>
  <p class="address">Po box 4172, Harwood Bay,<br>nsw 2519</p>
  <div class="rule rule--lower"></div>
</section>

</body>
</html>
```